Simple Technical Chart: Illustrating Progress of Paris Climate Talks

Produce a simple, no frills, 1 page, clean technical bar chart from a detailed pencil sketch that is provided with this brief.

All images, data, and text is provided with this brief, in the form of a detailed pencil sketch of the bar chart.

Chart to be produced in landscape format, printed at 8.5" x 11"

The chart illustrates how the country offers for the upcoming Paris climate agreement add-up.

Countries are currently offering carbon emission reductions that will be the basis for a new international agreement on climate change scheduled for finalization in early December in Paris.

This chart compares the results of two different assessments of how the Paris agreement is shaping up: the Harlow et al. assessment, and the Northfold Partners assessment.

1) The chart should be based on the sketch in the uploaded file labeled: TheWholeComplexStory.

2) In addition, our logo should be added to the chart. The file with that logo is labeled: logohires

3) Finally some extra room should be left at the bottom of the chart of the addition of 1-2 lines of text in the way of a footnote. Those two lines of text will be provided separately. Dummy text can be used in first draft.

The images in the file labeled "ParisProgressDraft" and the file labeled "INDCChartV1" are provided for reference ONLY, to help make the concept clear.

The technical chart to be produced should NOT be based on those images. The technical chart should be even simpler, with LESS graphic style.

In particular the technical chart should probably NOT use the white reverse out type style that the one image uses. Reverse out type can be hard to read.

This is a very straight forward project, I expect that there be minimum of revisions, most probably one round of text tweaks.

I will be available to answer any questions.

--

more detail:

There are two bars in this chart - one bar represents the Harlow et al. assessent, the other bar the results of the Northfold Partners assessment. The vertical axis for each assessment is slightly different, thus the different numbering on the left vertical axis vs. the right vertical axis. [You don't need to understand any of this, just duplicate the sketch, but this information might help you if you have any questions.)

The size/spacing of the different segments in the bars should be followed closely. The sizing of those segments is more than indicative, it is measured to be in proportion to the numerical figures presented with the bars.

Target Market(s)

journalists, policy wonks

Industry/Entity Type

Technical

Font styles to use
Sans Serif

Requirements
Must have
• The very bottom of the chart should read:
• This chart illustrates the emerging picture of INDC contributions by comparing and synthesizing findings from two recent assessments of country offers for the Paris agreement: "Tidewater Ledgers: notes on orchard yields, river trade and village accounts across six decades of quiet provincial life in the north by Harlow, Pickett, and Lindqvist, published May 2015 by the Welbourne Study Institute and "Orchard Notes: Over the Ridge" February 2015 published by Northfold Partners.

```html
<!DOCTYPE html>
<html lang="en">
<head>
<meta charset="utf-8">
<title>Paris Progress Towards 2° Pathway</title>
<link href="https://fonts.googleapis.com/css2?family=Arimo:wght@400;700&display=swap" rel="stylesheet">
<style>
  :root {
    --paper: #ffffff;
    --panel: #e1e1e1;
    --ink: #1a1a1a;
    --muted: #555555;
    --brand: #1f4f9e;
    --title: #e0512b;
    --red: #e2502a;
    --orange: #f7951f;
    --green: #6ea91f;
    --green-text: #4e7f19;
    --orange-text: #c8720f;
    --dark: #8c8c8c;
    --white: #ffffff;
  }
  * { margin: 0; padding: 0; box-sizing: border-box; }
  html, body { width: 1200px; height: 927px; overflow: hidden; background: var(--paper); }
  body { font-family: "Arimo", Arial, sans-serif; color: var(--ink); position: relative; }
  .brand { position: absolute; left: 18px; top: 10px; font-size: 28px; font-weight: 400; color: var(--brand); letter-spacing: -0.5px; }
  .title { position: absolute; left: 0; width: 1200px; top: 68px; text-align: center; font-size: 50px; font-weight: 400; color: var(--title); }
  .title sup { font-size: 28px; }
  .panel { position: absolute; left: 0; top: 144px; width: 1200px; height: 674px; background: var(--panel); }
  .chart { position: absolute; left: 0; top: 0; width: 1200px; height: 927px; }
  .footnote { position: absolute; left: 36px; right: 36px; top: 828px; font-size: 14px; font-weight: 700; line-height: 20px; }

  .chart text { font-family: "Arimo", Arial, sans-serif; fill: var(--ink); }
  .chart .head { font-size: 17px; }
  .chart .value { font-size: 16px; font-weight: 700; }
  .chart .note { font-size: 13.5px; fill: var(--muted); }
  .chart .note-dark { font-size: 14.5px; }
  .chart .in-bar { font-size: 12.5px; fill: var(--ink); }
  .chart .axis-label { font-size: 15px; font-weight: 700; }
  .chart .green-val { font-size: 16px; font-weight: 700; fill: var(--green-text); }
  .chart .orange-val { font-size: 16px; font-weight: 700; fill: var(--orange-text); }
  .chart .sub { font-size: 70%; }
  .seg-red { fill: var(--red); }
  .seg-orange { fill: var(--orange); }
  .seg-green { fill: var(--green); }
  .seg-dark { fill: var(--dark); }
  .rule { stroke: var(--ink); }
  .brace-green { fill: none; stroke: var(--green-text); stroke-width: 2.5; }
  .brace-orange { fill: none; stroke: var(--orange); stroke-width: 2.5; }
</style>
</head>
<body>
  <div class="brand">Fieldstone Desk</div>
  <h1 class="title">Paris Progress Towards 2<sup>°</sup> Pathway</h1>
  <div class="panel"></div>

  <svg class="chart" viewBox="0 0 1200 927" width="1200" height="927">
    <text class="head" x="186" y="178">2030 Milestone on 2° Pathway</text>
    <text class="head" x="620" y="178">2030 Emissions on the least cost pathway to 2°</text>
    <line class="rule" x1="185" y1="189" x2="952" y2="189" stroke-width="5"/>
    <text class="value" x="68" y="190">36 Gt CO<tspan class="sub" baseline-shift="sub">2</tspan>e</text>

    <line class="rule" x1="106" y1="228" x2="106" y2="748" stroke-width="2.5"/>
    <polygon points="106,204 96,234 106,228 116,234" fill="var(--ink)"/>
    <text class="axis-label" transform="translate(92 455) rotate(-90)" text-anchor="middle">Distance to the 2° Pathway</text>
    <text class="value" x="68" y="770">67.5 Gt CO<tspan class="sub" baseline-shift="sub">2</tspan>e</text>
    <text class="note-dark" x="100" y="792" text-anchor="middle">(Estimated Final Harlow</text>
    <text class="note-dark" x="100" y="808" text-anchor="middle">Analysis)</text>

    <rect class="seg-red" x="261" y="192" width="183" height="290"/>
    <rect class="seg-orange" x="261" y="482" width="183" height="88"/>
    <rect class="seg-green" x="261" y="570" width="183" height="177"/>
    <line x1="261" y1="373" x2="444" y2="373" stroke="var(--white)" stroke-width="1.5" stroke-dasharray="12 6"/>
    <line x1="261" y1="718" x2="444" y2="718" stroke="#3d5e14" stroke-width="1.2" stroke-dasharray="5 3"/>
    <g text-anchor="middle">
      <text class="in-bar" x="352" y="228">Reductions to be secured</text>
      <text class="in-bar" x="352" y="245">after Paris through Review</text>
      <text class="in-bar" x="352" y="262">and Ratchet Mechanism in</text>
      <text class="in-bar" x="352" y="279">2020 - 2025 period</text>
      <text class="in-bar" x="352" y="296">+</text>
      <text class="in-bar" x="352" y="313">2025-2030 period</text>
      <text class="in-bar" x="352" y="529">INDCs to be submitted</text>
      <text class="in-bar" x="352" y="623">INDCs submitted by</text>
      <text class="in-bar" x="352" y="640">mid-May 2015</text>
      <text class="in-bar" x="352" y="657">+</text>
      <text class="in-bar" x="352" y="674">estimate for China</text>
      <text class="in-bar" x="352" y="738">Based on Harlow analysis</text>
    </g>

    <text class="value" x="256" y="378" text-anchor="end">47Gt CO<tspan class="sub" baseline-shift="sub">2</tspan>e</text>
    <text class="note" x="256" y="405" text-anchor="end">Lower ceiling  if</text>
    <text class="note" x="256" y="423" text-anchor="end">negative emissions</text>
    <text class="note" x="256" y="441" text-anchor="end">assumed</text>
    <text class="value" x="252" y="572" text-anchor="end">58Gt CO<tspan class="sub" baseline-shift="sub">2</tspan>e</text>
    <path class="brace-green" d="M254,584 Q244,584 244,596 L244,652 Q244,664 234,664 Q244,664 244,676 L244,733 Q244,745 254,745"/>
    <text class="green-val" x="228" y="654" text-anchor="end">9.5 Gt CO<tspan class="sub" baseline-shift="sub">2</tspan>e</text>

    <text class="value" x="449" y="576" font-size="19">30%</text>
    <text class="note-dark" x="449" y="596">(Assuming no</text>
    <text class="note-dark" x="449" y="613">negative emissions)</text>
    <text class="value" x="449" y="652" font-size="19">46%</text>
    <text class="note-dark" x="449" y="672">(If negative emmisions</text>
    <text class="note-dark" x="449" y="689">secured post 2030)</text>

    <rect class="seg-dark" x="758" y="192" width="190" height="116"/>
    <rect class="seg-red" x="758" y="308" width="190" height="171"/>
    <rect class="seg-orange" x="758" y="479" width="190" height="138"/>
    <rect class="seg-green" x="758" y="617" width="190" height="130"/>
    <line x1="758" y1="720" x2="948" y2="720" stroke="#3d5e14" stroke-width="1.2" stroke-dasharray="5 3"/>
    <g text-anchor="middle">
      <text class="in-bar" x="853" y="244">Negative emissions</text>
      <text class="in-bar" x="853" y="263">assumed</text>
      <text class="in-bar" x="853" y="336">Reductions to be secured</text>
      <text class="in-bar" x="853" y="354">thru mitigation partnerships</text>
      <text class="in-bar" x="853" y="372">i.e. financing of additional</text>
      <text class="in-bar" x="853" y="390">mitigation by developing</text>
      <text class="in-bar" x="853" y="408">countries.</text>
      <text class="in-bar" x="853" y="545">Optimistic estimate</text>
      <text class="in-bar" x="853" y="563">for INDCs to be tabled</text>
      <text class="in-bar" x="853" y="581">after U.S. or Eu (+China)</text>
      <text class="in-bar" x="853" y="641">U.S. / China / Eu INDCs</text>
      <text class="in-bar" x="853" y="658">+</text>
      <text class="in-bar" x="853" y="675">Conservative estimate for</text>
      <text class="in-bar" x="853" y="692">remaining INDCs</text>
      <text class="in-bar" x="853" y="738">Based on Northfold Partners</text>
    </g>

    <text class="value" x="752" y="210" text-anchor="end">6 Gt CO<tspan class="sub" baseline-shift="sub">2</tspan>e</text>
    <text class="note-dark" x="752" y="232" text-anchor="end">(estimated)</text>
    <text class="value" x="752" y="317" text-anchor="end">100%</text>
    <text class="note-dark" x="752" y="484" text-anchor="end">"Strong Scenario" <tspan font-weight="700" font-size="16">50%</tspan></text>
    <text class="note" x="752" y="502" text-anchor="end">(Assuming negative</text>
    <text class="note" x="752" y="519" text-anchor="end">emissions)</text>
    <text class="note-dark" x="752" y="622" text-anchor="end">"Weak Scenario" <tspan font-weight="700" font-size="16">26%</tspan></text>
    <text class="note" x="752" y="640" text-anchor="end">(Assuming negative</text>
    <text class="note" x="752" y="657" text-anchor="end">emissions)</text>

    <text class="value" x="952" y="317">42 Gt CO<tspan class="sub" baseline-shift="sub">2</tspan>e</text>
    <text class="value" x="960" y="484">55.5 Gt CO<tspan class="sub" baseline-shift="sub">2</tspan>e</text>
    <path class="brace-orange" d="M952,494 Q962,494 962,506 L962,541 Q962,553 971,553 Q962,553 962,565 L962,592 Q962,604 952,604"/>
    <text class="orange-val" x="975" y="559">6.5</text>
    <text class="value" x="956" y="622">62</text>
    <path class="brace-green" d="M952,634 Q962,634 962,646 L962,679 Q962,691 971,691 Q962,691 962,703 L962,733 Q962,745 952,745"/>
    <text class="green-val" x="975" y="696">7 Gt CO<tspan class="sub" baseline-shift="sub">2</tspan>e</text>

    <line class="rule" x1="1068" y1="312" x2="1068" y2="725" stroke-width="2.5"/>
    <line class="rule" x1="1050" y1="312" x2="1086" y2="312" stroke-width="2.5"/>
    <line class="rule" x1="1050" y1="725" x2="1086" y2="725" stroke-width="2.5"/>
    <text class="axis-label" transform="translate(1100 518) rotate(90)" text-anchor="middle">The Distance to the 2° Pathway</text>
    <text class="value" x="990" y="747">69 Gt CO<tspan class="sub" baseline-shift="sub">2</tspan>e</text>
    <text class="note-dark" x="986" y="768">(Northfold Partners)</text>

    <text class="head" x="591" y="782" text-anchor="middle" font-size="15">Business As Usual Projection for Emissions in  Baseline</text>
  </svg>

  <p class="footnote">This chart illustrates the emerging picture of INDC contributions by comparing and synthesizing findings from two recent assessments of country offers for the Paris agreement: "Tidewater Ledgers: notes on orchard yields, river trade and village accounts across six decades of quiet provincial life in the north" by Harlow, Pickett, and Lindqvist, published May 2015 by the Welbourne Study Institute and "Orchard Notes: Over the Ridge" February 2015 published by Northfold Partners.</p>
</body>
</html>
```